Dinner Invitation for an email

Please create an image I can embed in an email. The tone should be sophisticated, fun and festive.

Here is the copy:

FOOD | FRIENDS | FUN
Please join QBR and friends at Corvell's Harbor Room for cocktails, conversation and a delectable dinner
Date: Monday, January 23 (during NPDF)
Time: Cocktails start at 6:30 | Dinner is around 7
Place: Corvell's Harbor Room - The Pearl Terrace
27318 W Bramwick Pkwy - Scottsdale
(Adjacent to the Halloway Brightmere Lodge)

RSVP: nora.whitby@qbrvantage.com
(Nora will send you a calendar invite)

Hope to see you there!

```html
<!DOCTYPE html>
<html lang="en">
<head>
<meta charset="utf-8">
<title>Food | Friends | Fun – Dinner Invitation</title>
<link href="https://fonts.googleapis.com/css2?family=Tenor+Sans&family=Libre+Baskerville&family=Poppins:wght@400;600;700&display=swap" rel="stylesheet">
<style>
  :root {
    --bg: #221b16;
    --band: rgba(222, 216, 206, 0.72);
    --band-ink: #3a3128;
    --white: #ffffff;
    --cream: #f2e4c6;
    --muted: #e6ded2;
  }
  * { margin: 0; padding: 0; box-sizing: border-box; }
  html, body { width: 848px; height: 1200px; overflow: hidden; background: var(--bg); }
  .invite { position: relative; width: 848px; height: 1200px; background: var(--bg); overflow: hidden; }

  .hero-photo {
    position: absolute; left: 85px; top: 85px; width: 679px; height: 641px;
    background:
      radial-gradient(ellipse at 40% 35%, rgba(214,186,130,0.55), transparent 55%),
      radial-gradient(ellipse at 70% 70%, rgba(170,140,90,0.5), transparent 60%),
      linear-gradient(180deg, #6e5f4c 0%, #5a4c3b 45%, #3a3129 100%);
  }
  .title-band {
    position: absolute; left: 85px; top: 299px; width: 679px; height: 111px;
    background: var(--band);
    display: flex; align-items: center; justify-content: center;
  }
  .title-band h1 {
    font-family: "Tenor Sans", sans-serif; font-weight: 400;
    font-size: 56px; color: var(--band-ink); letter-spacing: -1px; white-space: nowrap;
  }
  .title-band .sep { font-size: 26px; vertical-align: middle; margin: 0 8px; position: relative; top: -4px; }

  .snowflake { position: absolute; border-radius: 50%;
    background: radial-gradient(circle, rgba(255,255,255,0.85) 0%, rgba(255,255,255,0.35) 45%, rgba(255,255,255,0) 72%); }
  .snow-1 { left: 162px; top: 34px; width: 90px; height: 100px; }
  .snow-2 { left: 718px; top: 480px; width: 92px; height: 102px; }
  .snow-3 { left: 0; top: 600px; width: 138px; height: 166px; }
  .snow-4 { left: 681px; top: 1006px; width: 82px; height: 98px; }

  .lead {
    position: absolute; left: 0; top: 664px; width: 848px;
    font-family: "Libre Baskerville", serif; font-size: 21px; line-height: 31px;
    letter-spacing: 4px; text-transform: uppercase; text-align: center; color: var(--white);
  }
  .when {
    position: absolute; left: 0; top: 860px; width: 848px; text-align: center;
    font-family: "Poppins", sans-serif; font-weight: 700; font-size: 19px; line-height: 30px;
    color: var(--white); text-transform: uppercase;
  }
  .place {
    position: absolute; left: 0; top: 962px; width: 848px; text-align: center;
    font-family: "Poppins", sans-serif; font-weight: 600; font-size: 13.5px; line-height: 20.5px;
    letter-spacing: 2.6px; color: var(--cream); text-transform: uppercase;
  }
  .rsvp {
    position: absolute; left: 0; top: 1062px; width: 848px; text-align: center;
    font-family: "Poppins", sans-serif; font-weight: 600; font-size: 18px;
    letter-spacing: 2.6px; color: var(--cream);
  }
  .rsvp-note {
    position: absolute; left: 0; top: 1105px; width: 848px; text-align: center;
    font-family: "Poppins", sans-serif; font-weight: 400; font-size: 15.5px;
    color: var(--muted); text-transform: uppercase;
  }
  .sign-off {
    position: absolute; left: 0; top: 1145px; width: 848px; text-align: center;
    font-family: "Libre Baskerville", serif; font-size: 17px;
    letter-spacing: 3px; color: var(--white); text-transform: uppercase;
  }
</style>
</head>
<body>
<main class="invite">
  <div class="hero-photo" role="img" aria-label="Two champagne flutes with golden streamers and warm bokeh lights"></div>
  <div class="title-band">
    <h1>FOOD<span class="sep">|</span>FRIENDS<span class="sep">|</span>FUN</h1>
  </div>

  <div class="snowflake snow-1" role="img" aria-label="White snowflake"></div>
  <div class="snowflake snow-2" role="img" aria-label="White snowflake"></div>
  <div class="snowflake snow-3" role="img" aria-label="White snowflake"></div>
  <div class="snowflake snow-4" role="img" aria-label="White snowflake"></div>

  <p class="lead">Please join QBR and<br>friends at Corvell's<br>Harbor Room for cocktails,<br>conversation and a<br>delectable dinner</p>

  <p class="when">Date: Monday, January 23 (during NPDF)<br>Time: Cocktails start at 6:30 | Dinner is around 7</p>

  <p class="place">Place: Corvell's Harbor Room - The Pearl Terrace<br>27318 W Bramwick Pkwy - Scottsdale<br>(Adjacent to the Halloway Brightmere Lodge)</p>

  <p class="rsvp">RSVP: nora.whitby@qbrvantage.com</p>
  <p class="rsvp-note">(Nora will send you a calendar invite)</p>

  <p class="sign-off">Hope to see you there!</p>
</main>
</body>
</html>
```